We are in search of a new business card design for our business. We have a Mexican Grocery Store called Tortilla Grove Market, we would like to see that some have mexican design, but we are open to any type of designs.

Phone: to be announced
Fax: to be announced

Address is:
2415 Calloway Blvd
Harbor Point, MD 21099

```html
<!DOCTYPE html>
<html lang="en">
<head>
<meta charset="utf-8">
<title>Tortilla Grove Market — Business Card</title>
<link rel="stylesheet" href="https://fonts.googleapis.com/css2?family=Montserrat:wght@300;500;700&display=swap">
<style>
  :root {
    --page-bg: #e9e6e1;
    --card-bg: #fbfbfa;
    --brand-red: #d9262e;
    --rule: #3a3a3a;
    --muted: #6a6a6a;
    --band-black: #1d1d1d;
    --band-yellow: #f2b90f;
  }
  html, body {
    margin: 0;
    width: 1200px;
    height: 1022px;
    overflow: hidden;
    background: var(--page-bg);
    font-family: "Montserrat", sans-serif;
  }
  .card {
    position: absolute;
    left: 80px;
    top: 211px;
    width: 1040px;
    height: 600px;
    background: var(--card-bg);
    border-radius: 26px;
    overflow: hidden;
    box-shadow: 0 10px 30px rgba(0,0,0,0.15);
  }
  .card-art { position: absolute; inset: 0; }
  .brand {
    position: absolute;
    left: 50px;
    top: 262px;
    display: flex;
    align-items: center;
    gap: 14px;
  }
  .brand-dot {
    flex: none;
    width: 26px; height: 26px;
    border-radius: 50%;
    background: var(--brand-red);
  }
  .brand-name {
    font-weight: 700;
    font-size: 27px;
    line-height: 1.15;
    color: var(--brand-red);
    width: 220px;
  }
  .owner-name {
    position: absolute;
    left: 330px;
    width: 470px;
    top: 246px;
    margin: 0;
    text-align: right;
    font-weight: 500;
    font-size: 34px;
    line-height: 40px;
    letter-spacing: 1px;
    color: var(--brand-red);
    white-space: nowrap;
  }
  .owner-title {
    position: absolute;
    left: 760px;
    width: 90px;
    top: 306px;
    text-align: right;
    font-weight: 300;
    font-size: 24px;
    line-height: 30px;
    color: var(--muted);
  }
  .contact {
    position: absolute;
    left: 340px;
    top: 318px;
    font-weight: 300;
    font-size: 25px;
    line-height: 35px;
    color: var(--muted);
    white-space: nowrap;
  }
  .contact-line { display: flex; align-items: center; gap: 12px; }
  .contact-icon { width: 18px; height: 18px; fill: var(--brand-red); }
</style>
</head>
<body>
  <div class="card">
    <svg class="card-art" width="1040" height="600" viewBox="0 0 1040 600" aria-hidden="true">
      <line x1="330" y1="300" x2="830" y2="300" stroke="var(--rule)" stroke-width="2"/>
      <path d="M800,600 C900,470 950,300 962,70 L1040,70 L1040,600 Z" fill="var(--band-yellow)"/>
      <path d="M840,600 C930,470 972,300 978,70 L1040,70 L1040,600 Z" fill="var(--band-black)"/>
      <circle cx="985" cy="0" r="40" fill="var(--band-yellow)" stroke="var(--band-black)" stroke-width="5"/>
    </svg>

    <div class="brand">
      <span class="brand-dot"></span>
      <span class="brand-name">Tortilla Grove Market</span>
    </div>

    <h1 class="owner-name">MATEO REYES</h1>
    <span class="owner-title">Owner</span>

    <div class="contact">
      <div class="contact-line">2415 Calloway Blvd</div>
      <div class="contact-line">Harbor Point, MD 21099</div>
      <div class="contact-line">
        <svg class="contact-icon" viewBox="0 0 24 24"><path d="M6.6 10.8a15 15 0 0 0 6.6 6.6l2.2-2.2c.3-.3.7-.4 1-.2 1.1.4 2.3.6 3.6.6.6 0 1 .4 1 1V20c0 .6-.4 1-1 1A17 17 0 0 1 3 4c0-.6.4-1 1-1h3.5c.6 0 1 .4 1 1 0 1.3.2 2.5.6 3.6.1.3 0 .7-.2 1z"/></svg>
        410.555.0100
      </div>
      <div class="contact-line">
        <svg class="contact-icon" viewBox="0 0 24 24"><path d="M7 3h10v5H7zM5 9h14a2 2 0 0 1 2 2v6h-4v4H7v-4H3v-6a2 2 0 0 1 2-2zm4 8v2h6v-2z"/></svg>
        410.555.0222
      </div>
    </div>
  </div>
</body>
</html>
```